Create a Big Data Website that is professional but has a creative flare to it.

I am after a modern business design for a company in the Big Data space however it still needs to have a wow value and something stand out from other corporate websites.
My competitors websites are to give you and idea of content:
www.fendralux.com
www.vornuby.com
www.quillmerq4.com.au
www.tessovant.com
I have uploaded my company Logo so you can use that to make sure it matches your theme.

Target Market(s)

Banks, Insurance Companies, Government, Gas and Energy Companies and Food Manufacturing.

Industry/Entity Type

Consulting

Number of Pages Required

5+ page

Colors

Designer to choose colors to be used in the design.

Requirements
Must have
• Images, Diagrams around Big Data. Usage of information or graphs from sources like Pellwick are fine to use.
Nice to have
• Interactive design use mouse overs, change in text, highlighting information for clear focus.
Should not have
• Cluttered Pages of Informaiton

```html
<!DOCTYPE html>
<html lang="en">
<head>
<meta charset="utf-8">
<title>Veltrano Consulting Services</title>
<link href="https://fonts.googleapis.com/css2?family=Open+Sans:wght@400;600;700;800&display=swap" rel="stylesheet">
<style>
:root{
  --navy:#1c3f73;
  --navy-deep:#163560;
  --blue:#1b8bd6;
  --blue-bright:#1e9ae6;
  --ink:#222;
  --muted:#8a8f96;
  --pale:#eef0f3;
  --topbar:#333;
  --bottombar:#2b2b2b;
  --white:#fff;
  --ring:#9a9ea4;
}
*{box-sizing:border-box;margin:0;padding:0}
html,body{width:1200px;height:3243px;overflow:hidden}
body{position:relative;font-family:"Open Sans",Arial,sans-serif;color:var(--ink);background:var(--white)}
.abs{position:absolute}
.topbar{left:0;top:0;width:1200px;height:35px;background:var(--topbar);color:var(--white);font-size:13px}
.topbar .mail{left:119px;top:8px}
.topbar .phone{left:548px;top:8px}
.social{display:flex;gap:7px}
.social span{width:20px;height:20px;border:1.5px solid var(--white);border-radius:50%;display:block}
.topbar .social{left:950px;top:7px}
.header{left:0;top:35px;width:1200px;height:121px;background:var(--white)}
.brand{display:flex;align-items:center;gap:12px}
.brand .mark{width:50px;height:50px;background:var(--navy);display:block}
.brand .name{font-weight:800;font-size:38px;color:var(--navy);line-height:1}
.brand .tag{font-size:12px;font-weight:600;color:var(--blue);letter-spacing:1.5px}
.header .brand{left:119px;top:33px}
.nav{left:458px;top:50px;display:flex;gap:26px;font-size:15px;font-weight:600;color:var(--ink)}
.nav .active{color:var(--navy);border-bottom:3px solid var(--blue);padding-bottom:6px}
.quote{left:949px;top:45px;width:130px;height:37px;background:var(--blue);color:var(--white);font-size:14px;font-weight:600;border-radius:4px;display:flex;align-items:center;justify-content:center}
.hero{left:0;top:156px;width:1200px;height:402px;background:linear-gradient(120deg,#20477a 0%,#3c6fa4 45%,#5f8fbf 70%,#2a5788 100%)}
.hero-copy{left:300px;top:166px;width:584px;text-align:center;color:var(--white)}
.hero-copy h1{font-size:36px;font-weight:700}
.hero-copy p{font-size:14px;font-weight:600;line-height:18px;margin-top:8px}
.btn{display:inline-flex;align-items:center;gap:14px;height:28px;padding:0 10px;background:var(--navy);color:var(--white);font-size:11px;font-weight:700}
.btn .arrow{background:var(--blue);height:28px;width:36px;margin-right:-10px;display:flex;align-items:center;justify-content:center}
.hero-copy .btn{margin-top:16px}
.dots{left:562px;top:580px;display:flex;gap:8px}
.dots span{width:12px;height:12px;border-radius:50%;background:var(--navy)}
.dots span.on{background:var(--blue)}
.section-title{width:1200px;left:0;text-align:center;color:var(--navy);font-size:34px;font-weight:700}
.section-sub{width:1200px;left:0;text-align:center;color:var(--muted);font-size:14px}
.service{top:718px;width:340px;height:261px;text-align:center}
.service.featured{background:var(--pale)}
.service svg{margin-top:30px}
.service h3{font-size:16px;font-weight:600;color:var(--ink);margin-top:6px}
.service .rule{width:46px;height:3px;background:var(--blue);margin:10px auto 14px}
.service p{font-size:13px;color:var(--muted);line-height:17px;width:230px;margin:0 auto}
.service .more{font-size:14px;font-weight:600;margin-top:12px;display:flex;justify-content:center;align-items:center;gap:6px}
.band{left:0;top:1020px;width:1200px;height:403px;background:linear-gradient(100deg,#c9d2db 0%,#a8bccf 40%,#e3e8ee 75%,#b9c6d2 100%)}
.band-panel{left:86px;top:1057px;width:513px;height:327px;background:rgba(28,70,130,.92);color:var(--white);padding:44px 36px}
.band-panel h2{font-size:34px;font-weight:700;line-height:42px}
.band-panel p{font-size:13px;font-weight:600;line-height:17px;margin-top:16px}
.band-panel .btn{margin-top:24px}
.step{font-size:13px;line-height:17px;color:var(--muted);text-align:center;width:190px}
.step b{display:block;color:var(--ink);font-size:15px;font-weight:700;margin-bottom:3px}
.news{left:0;top:1915px;width:1200px;height:403px;background:linear-gradient(180deg,#1e4a82 0%,#1a3f70 100%)}
.news .section-title,.news .section-sub{color:var(--white)}
.news-panel{left:121px;top:2039px;width:960px;height:290px;background:var(--white);box-shadow:0 2px 8px rgba(0,0,0,.15)}
.card{top:2078px;width:191px}
.card .photo{height:127px;background:linear-gradient(135deg,#2f5d8e,#8fb2d2)}
.card h4{font-size:13px;font-weight:700;margin-top:10px}
.card .sub{font-size:13px;margin-top:4px}
.card .meta{font-size:12px;color:var(--muted);display:flex;justify-content:space-between;margin-top:6px}
.card .meta em{font-style:normal;color:var(--blue)}
.chev{top:2308px;color:var(--muted);font-size:14px}
.client{width:221px;height:113px;background:var(--pale);display:flex;align-items:center;justify-content:center;gap:10px;font-size:22px;font-weight:600;color:#555}
.client i{width:28px;height:28px;border-radius:50%;background:#555;display:block}
.footer{left:0;top:2880px;width:1200px;height:305px;background:var(--navy);color:var(--white)}
.footer-brand{left:0;top:2925px;width:352px;height:67px;background:var(--white);padding:10px 0 0 119px}
.footer-brand .mark{width:38px;height:38px}
.footer-brand .name{font-size:30px}
.footer-brand .tag{font-size:10px}
.footer-about{left:119px;top:3012px;width:250px;font-size:14px;font-weight:600;line-height:19px}
.footer-more{left:119px;top:3090px;font-size:14px;font-weight:700}
.fcol h5{font-size:14px;font-weight:700;letter-spacing:.5px;margin-bottom:16px}
.fcol li{list-style:none;font-size:13px;line-height:24px}
.contact li{display:flex;gap:10px;align-items:flex-start;font-size:14px;line-height:20px;margin-bottom:4px}
.newsletter p{font-size:13px;line-height:18px;width:230px}
.subscribe{display:flex;margin-top:10px}
.subscribe .field{width:182px;height:32px;background:var(--white);color:var(--muted);font-size:11px;font-style:italic;padding:9px 8px}
.subscribe .go{width:35px;height:32px;background:var(--blue);margin-left:2px;display:flex;align-items:center;justify-content:center}
.bottombar{left:0;top:3185px;width:1200px;height:58px;background:var(--bottombar);color:var(--white);font-size:15px;font-weight:600}
.bottombar .copy{left:121px;top:18px}
.bottombar .social{left:866px;top:14px;gap:12px}
.bottombar .social span{width:28px;height:28px}
</style>
</head>
<body>

<div class="abs topbar">
  <span class="abs mail">info@veltrano</span>
  <span class="abs phone">0 (123) 456-7890</span>
  <div class="abs social"><span></span><span></span><span></span><span></span><span></span></div>
</div>

<header class="abs header">
  <div class="abs brand">
    <span class="mark"></span>
    <div><div class="name">veltrano</div><div class="tag">CONSULTING SERVICES</div></div>
  </div>
  <nav class="abs nav">
    <span class="active">About</span><span>Our Services</span><span>Big Data</span><span>News</span><span>Clients</span><span>Contact</span>
  </nav>
  <div class="abs quote">Get a Quote</div>
</header>

<section class="abs hero" role="img" aria-label="Blue-toned photo of business charts and data graphs over a world map"></section>
<div class="abs hero-copy">
  <h1>Business Intelligence</h1>
  <p>Lorem Ipsum is simply dummy text of the printing and industry.<br>Lorem Ipsum has been the industry's</p>
  <span class="btn">Read More <span class="arrow"><svg width="14" height="10" viewBox="0 0 14 10"><path d="M0 5h12M8 1l4 4-4 4" stroke="#fff" stroke-width="1.6" fill="none"/></svg></span></span>
</div>
<div class="abs dots"><span class="on"></span><span></span><span></span><span></span></div>

<h2 class="abs section-title" style="top:628px">Our Services</h2>
<p class="abs section-sub" style="top:674px">Lorem Ipsum is simply dummy text of the printing and industry.</p>

<div class="abs service" style="left:70px">
  <svg width="40" height="42" viewBox="0 0 40 42"><g fill="none" stroke="#222" stroke-width="2"><rect x="4" y="3" width="32" height="11" rx="2"/><rect x="4" y="16" width="32" height="11" rx="2"/><rect x="4" y="29" width="32" height="11" rx="2"/><path d="M9 8h10M9 21h10M9 34h10"/></g></svg>
  <h3>BIG DATA</h3><div class="rule"></div>
  <p>Lorem Ipsum is simply dummy text of the printing and industry .. has been the industry's</p>
  <div class="more">Read More.. <svg width="18" height="18" viewBox="0 0 18 18"><circle cx="9" cy="9" r="8" stroke="#222" stroke-width="1.5" fill="none"/><path d="M5 9h7M9 6l3 3-3 3" stroke="#222" stroke-width="1.5" fill="none"/></svg></div>
</div>
<div class="abs service featured" style="left:432px">
  <svg width="44" height="42" viewBox="0 0 44 42"><g stroke="#1b8bd6" stroke-width="2"><path d="M22 4v34M5 21h34M10 9l24 24M34 9L10 33"/></g><circle cx="22" cy="21" r="10" fill="#1b8bd6"/></svg>
  <h3>BUSINESS INTELLIGENCE</h3><div class="rule"></div>
  <p>Lorem Ipsum is simply dummy text of the printing and industry .. has been the industry's</p>
  <div class="more">Read More.. <svg width="18" height="18" viewBox="0 0 18 18"><circle cx="9" cy="9" r="8" stroke="#222" stroke-width="1.5" fill="none"/><path d="M5 9h7M9 6l3 3-3 3" stroke="#222" stroke-width="1.5" fill="none"/></svg></div>
</div>
<div class="abs service" style="left:788px">
  <svg width="44" height="42" viewBox="0 0 44 42"><path d="M12 32a8 8 0 0 1 0-16 11 11 0 0 1 21 2 7 7 0 0 1 0 14z" fill="none" stroke="#222" stroke-width="2"/><path d="M18 24a5 5 0 0 1 9-2M27 22v-4M26 28a5 5 0 0 1-9 2M17 30v4" stroke="#222" stroke-width="2" fill="none"/></svg>
  <h3>CLOUD</h3><div class="rule"></div>
  <p>Lorem Ipsum is simply dummy text of the printing and industry .. has been the industry's</p>
  <div class="more">Read More.. <svg width="18" height="18" viewBox="0 0 18 18"><circle cx="9" cy="9" r="8" stroke="#222" stroke-width="1.5" fill="none"/><path d="M5 9h7M9 6l3 3-3 3" stroke="#222" stroke-width="1.5" fill="none"/></svg></div>
</div>

<section class="abs band" role="img" aria-label="Photo of a hand touching a tablet showing line charts"></section>
<div class="abs band-panel">
  <h2>Big Data Analytics<br>SOLUTIONS</h2>
  <p>Lorem Ipsum is simply dummy text of the printing and typesetting industry. Lorem Ipsum has been the industry's standard dummy text ever since the 1500s, when an unknown printer took a galley of type and scrambled it to make a type specimen book. It has survived not only five centuries, geMaker including versions of Lorem Ipsum.</p>
  <span class="btn">Read More <span class="arrow"><svg width="14" height="10" viewBox="0 0 14 10"><path d="M0 5h12M8 1l4 4-4 4" stroke="#fff" stroke-width="1.6" fill="none"/></svg></span></span>
</div>

<svg class="abs" style="left:0;top:1500px" width="1200" height="360" viewBox="0 1500 1200 360">
  <g stroke="var(--ring)" stroke-width="7" fill="none">
    <path d="M123 1676H1060"/>
    <path d="M123 1662v28"/>
    <path d="M1060 1664l18 12-18 12z" fill="var(--ring)"/>
    <circle cx="242" cy="1589" r="70" stroke-dasharray="370 70"/>
    <circle cx="579" cy="1589" r="70" stroke-dasharray="370 70"/>
    <circle cx="930" cy="1589" r="70" stroke-dasharray="370 70"/>
    <circle cx="417" cy="1755" r="70" stroke-dasharray="370 70" transform="rotate(180 417 1755)"/>
    <circle cx="757" cy="1755" r="70" stroke-dasharray="370 70" transform="rotate(180 757 1755)"/>
  </g>
  <g>
    <circle cx="242" cy="1589" r="52" fill="var(--blue)"/><circle cx="242" cy="1589" r="36" fill="var(--navy)"/>
    <circle cx="579" cy="1589" r="52" fill="var(--blue)"/><circle cx="579" cy="1589" r="36" fill="var(--navy)"/>
    <circle cx="930" cy="1589" r="52" fill="var(--blue)"/><circle cx="930" cy="1589" r="36" fill="var(--navy)"/>
    <circle cx="417" cy="1755" r="52" fill="var(--blue)"/><circle cx="417" cy="1755" r="36" fill="var(--navy)"/>
    <circle cx="757" cy="1755" r="52" fill="var(--blue)"/><circle cx="757" cy="1755" r="36" fill="var(--navy)"/>
  </g>
  <g stroke="#fff" stroke-width="2" fill="none">
    <rect x="229" y="1579" width="26" height="18"/><path d="M234 1592v-5M240 1592v-8M246 1592v-3"/>
    <rect x="572" y="1574" width="14" height="9"/><rect x="562" y="1597" width="12" height="9"/><rect x="584" y="1597" width="12" height="9"/><path d="M579 1583v7M568 1597v-7h22v7"/>
    <circle cx="930" cy="1580" r="6"/><path d="M918 1602a12 10 0 0 1 24 0M930 1570a19 19 0 1 1-0.1 0"/>
    <path d="M409 1765h16M411 1760a8 8 0 1 1 12 0v4h-12z"/>
    <rect x="742" y="1743" width="30" height="22" rx="2"/><path d="M746 1760l7-8 6 5 9-9"/>
  </g>
</svg>
<div class="abs step" style="left:320px;top:1552px;text-align:left;width:180px"><b>Data Enrichment</b>Lorem ipsum dolor sit amet, consectetur adipiscing elit, sed do eiusmod tempor</div>
<div class="abs step" style="left:666px;top:1552px;text-align:left;width:180px"><b>Data Visualisation</b>Lorem ipsum dolor sit amet, consectetur adipiscing elit, sed do eiusmod tempor</div>
<div class="abs step" style="left:154px;top:1700px"><b>Predictive Analytics</b>Lorem ipsum dolor sit amet, consectetur adipiscing elit, sed do eiusmod tempor</div>
<div class="abs step" style="left:500px;top:1700px;text-align:left;width:180px"><b>Data Governance</b>Lorem ipsum dolor sit amet, consectetur adipiscing elit, sed do eiusmod tempor</div>
<div class="abs step" style="left:845px;top:1700px;text-align:left;width:180px"><b>Automated CRM</b>Lorem ipsum dolor sit amet, consectetur adipiscing elit, sed do eiusmod tempor</div>

<section class="abs news" role="img" aria-label="Dark blue photo of a city skyline at night"></section>
<h2 class="abs section-title" style="top:1946px;color:#fff">Latest News</h2>
<p class="abs section-sub" style="top:1990px;color:#fff;font-weight:600">Lorem Ipsum is simply dummy text of the printing and industry.</p>
<div class="abs news-panel"></div>
<article class="abs card" style="left:164px"><div class="photo" role="img" aria-label="Photo of a glowing technology network"></div><h4>Lorem Ipsum is simply ?</h4><div class="sub">Then &amp; Now</div><div class="meta"><span>June 20, 2017</span><span>BY <em>JOHN</em></span></div></article>
<article class="abs card" style="left:391px"><div class="photo" role="img" aria-label="Photo of a circuit board with big data text"></div><h4>Lorem Ipsum is simply ?</h4><div class="sub">Then &amp; Now</div><div class="meta"><span>June 20, 2017</span><span>BY <em>JOHN</em></span></div></article>
<article class="abs card" style="left:620px"><div class="photo" role="img" aria-label="Photo of a business analyst viewing a chart display" style="background:linear-gradient(135deg,#9fbcd8,#e4edf5)"></div><h4>Lorem Ipsum is simply ?</h4><div class="sub">Then &amp; Now</div><div class="meta"><span>June 20, 2017</span><span>BY <em>JOHN</em></span></div></article>
<article class="abs card" style="left:852px"><div class="photo" role="img" aria-label="Photo of hands working on a laptop" style="background:linear-gradient(135deg,#6d7780,#c7ccd1)"></div><h4>Lorem Ipsum is simply ?</h4><div class="sub">Then &amp; Now</div><div class="meta"><span>June 20, 2017</span><span>BY <em>JOHN</em></span></div></article>
<span class="abs chev" style="left:247px">&#8964;</span><span class="abs chev" style="left:477px">&#8964;</span><span class="abs chev" style="left:706px">&#8964;</span><span class="abs chev" style="left:937px">&#8964;</span>
<div class="abs" style="left:547px;top:2365px"><span class="btn">View More <span class="arrow"><svg width="14" height="10" viewBox="0 0 14 10"><path d="M0 5h12M8 1l4 4-4 4" stroke="#fff" stroke-width="1.6" fill="none"/></svg></span></span></div>

<h2 class="abs section-title" style="top:2444px">OUR CLIENTS</h2>
<p class="abs section-sub" style="top:2492px">Lorem Ipsum is simply dummy text of the printing and industry.</p>
<div class="abs client" style="left:119px;top:2542px"><i></i>Quarnix</div>
<div class="abs client" style="left:361px;top:2542px"><i></i>Quarnix</div>
<div class="abs client" style="left:614px;top:2542px"><i></i>Quarnix</div>
<div class="abs client" style="left:858px;top:2542px"><i></i>Quarnix</div>
<div class="abs client" style="left:119px;top:2677px"><i></i>Quarnix</div>
<div class="abs client" style="left:361px;top:2677px"><i></i>Quarnix</div>
<div class="abs client" style="left:614px;top:2677px"><i></i>Quarnix</div>
<div class="abs client" style="left:858px;top:2677px"><i></i>Quarnix</div>

<footer class="abs footer"></footer>
<div class="abs footer-brand brand">
  <span class="mark"></span>
  <div><div class="name">veltrano</div><div class="tag">CONSULTING SERVICES</div></div>
</div>
<p class="abs footer-about" style="color:#fff">Lorem ipsum dolor sit amet sed conse ctetur adipisicingsed elit sed do eiusmod tempor dolore magna aliqua.</p>
<div class="abs footer-more" style="color:#fff">Read More.. &#8594;</div>
<div class="abs fcol" style="left:396px;top:2937px;color:#fff">
  <h5>QUICK LINKS</h5>
  <ul><li>&gt; About</li><li>&gt; Our Services</li><li>&gt; Big Data</li><li>&gt; News</li><li>&gt; Client</li><li>&gt; Contact</li></ul>
</div>
<div class="abs fcol contact" style="left:599px;top:2937px;color:#fff">
  <h5>CONTACT US</h5>
  <ul>
    <li><svg width="16" height="18" viewBox="0 0 16 18"><path d="M1 8l7-6 7 6v9H1z" fill="#fff"/></svg><span>123 ADDRESS,CITY,<br>STATE,ZIP</span></li>
    <li><svg width="16" height="16" viewBox="0 0 16 16"><path d="M3 1l3 4-2 2a10 10 0 0 0 5 5l2-2 4 3-2 2C7 15 1 9 1 3z" fill="#fff"/></svg><span>0 (123) 456-7890</span></li>
    <li><svg width="16" height="16" viewBox="0 0 16 16"><rect x="1" y="5" width="14" height="9" fill="#fff"/><rect x="4" y="1" width="8" height="4" fill="#fff"/></svg><span>0 (123) 456-7890</span></li>
    <li><svg width="16" height="16" viewBox="0 0 16 16"><rect x="1" y="3" width="14" height="10" fill="#fff"/><path d="M1 3l7 6 7-6" stroke="#1c3f73" fill="none"/></svg><span>INFO@VELTRANO.COM</span></li>
    <li><svg width="16" height="16" viewBox="0 0 16 16"><circle cx="8" cy="8" r="7" stroke="#fff" stroke-width="1.5" fill="none"/><path d="M1 8h14M8 1c-4 4-4 10 0 14M8 1c4 4 4 10 0 14" stroke="#fff" fill="none"/></svg><span>WWW.VELTRANO.COM</span></li>
  </ul>
</div>
<div class="abs fcol newsletter" style="left:860px;top:2937px;color:#fff">
  <h5>NEWSLETTER SUBSCRIBE</h5>
  <p>We will inform you about newset project and promotions.Subscribe to our newsletter.</p>
  <div class="subscribe"><div class="field">Your Email Address</div><div class="go"><svg width="16" height="12" viewBox="0 0 16 12"><rect x="1" y="1" width="14" height="10" fill="#fff"/><path d="M1 1l7 6 7-6" stroke="#1b8bd6" fill="none"/></svg></div></div>
</div>

<div class="abs bottombar">
  <span class="abs copy">© Copyright 2017 Veltrano.All rights Reserved.</span>
  <div class="abs social"><span></span><span></span><span></span><span></span><span></span></div>
</div>

</body>
</html>
```